distributor of aftermarket auto electrical components

I am after business card design for my new company called
Summit Vehicle Supplies (SVS as the acronym). I will supplying automotive wiring components, basically from battery to headlight. I will be aiming to sell in the 4wd scene and to auto electricians. i am not worried which colours are used though i would like it to be dynamic.
Updates

sorry guys, i have add a mobile and e-mail address that will need to on there as well. Sorry for theĀ inconvenience.

sorry guys i had erred on my spelling with my e-mail. i have now fixed it in the brief

Target Market(s)

4wd industry, custom cars, RV, auto electricians

Industry/Entity Type

Electrical

Requirements
Must have
• Company Name
ABN number: 71 306 548 290
Director: Derek Holloway
M 0432 718 946
E dhollo@fernwire.com.au

```html
<!DOCTYPE html>
<html lang="en">
<head>
<meta charset="utf-8">
<title>Summit Vehicle Supplies – Business Card</title>
<link href="https://fonts.googleapis.com/css2?family=Arimo:wght@400;700&display=swap" rel="stylesheet">
<style>
  :root {
    --stage: #d9d9d9;
    --navy-deep: #0a1730;
    --navy: #13284f;
    --navy-glow: #1f3d72;
    --white: #ffffff;
    --band-text: #9a9da3;
    --accent-red: #d0121b;
    --muted: #8d97a8;
  }
  html, body {
    margin: 0;
    padding: 0;
    width: 1200px;
    height: 1200px;
    overflow: hidden;
    background: var(--stage);
    font-family: "Arimo", Arial, sans-serif;
  }
  .stage {
    width: 1200px;
    height: 1200px;
    display: flex;
    flex-direction: column;
    align-items: center;
    justify-content: center;
    gap: 60px;
  }
  .card {
    position: relative;
    width: 840px;
    height: 512px;
    overflow: hidden;
    background: radial-gradient(ellipse at 60% 40%, var(--navy-glow) 0%, var(--navy) 45%, var(--navy-deep) 100%);
    box-shadow: 0 6px 18px rgba(0,0,0,0.25);
  }

  /* Back of card */
  .brand-mark {
    position: absolute;
    left: 0;
    right: 0;
    top: 170px;
    display: flex;
    flex-direction: column;
    align-items: center;
    gap: 28px;
  }
  .brand-dot {
    width: 64px;
    height: 64px;
    border-radius: 50%;
    background: var(--white);
  }
  .brand-name {
    margin: 0;
    color: var(--white);
    font-weight: 700;
    font-size: 50px;
    line-height: 1.1;
    letter-spacing: -0.5px;
  }

  /* Front of card */
  .acronym-row {
    position: absolute;
    left: 120px;
    top: 28px;
    height: 140px;
    display: flex;
    align-items: center;
    gap: 36px;
  }
  .acronym-dot {
    width: 56px;
    height: 56px;
    border-radius: 50%;
    background: var(--white);
  }
  .acronym {
    margin: 0;
    color: var(--white);
    font-weight: 700;
    font-size: 140px;
    line-height: 140px;
    letter-spacing: -2px;
  }
  .name-band {
    position: absolute;
    left: 0;
    right: 0;
    top: 190px;
    height: 70px;
    margin: 0;
    padding-left: 150px;
    box-sizing: border-box;
    background: var(--white);
    color: var(--band-text);
    font-weight: 700;
    font-size: 46px;
    line-height: 70px;
    letter-spacing: -0.5px;
    white-space: nowrap;
  }
  .contact {
    position: absolute;
    left: 50px;
    top: 280px;
  }
  .role,
  .person {
    margin: 0;
    font-weight: 700;
    font-size: 30px;
    line-height: 36px;
  }
  .role { color: var(--white); }
  .person {
    margin-bottom: 16px;
    color: var(--accent-red);
  }
  .detail {
    margin: 0;
    font-size: 18px;
    line-height: 24px;
  }
  .detail-label { color: var(--white); }
  .detail-value { color: var(--muted); }
  .abn-number { margin-bottom: 10px; }
</style>
</head>
<body>
<main class="stage">
  <section class="card card-back" aria-label="Business card back">
    <div class="brand-mark">
      <span class="brand-dot"></span>
      <p class="brand-name">Summit Vehicle Supplies</p>
    </div>
  </section>

  <section class="card card-front" aria-label="Business card front">
    <div class="acronym-row">
      <span class="acronym-dot"></span>
      <h1 class="acronym">SVS</h1>
    </div>
    <p class="name-band">Summit Vehicle Supplies</p>
    <div class="contact">
      <p class="role">Director</p>
      <p class="person">Derek Holloway</p>
      <p class="detail detail-label">ABN number</p>
      <p class="detail detail-value abn-number">71 306 548 290</p>
      <p class="detail detail-label">M <span class="detail-value">0432 718 946</span></p>
      <p class="detail detail-label">E <span class="detail-value">dhollo@fernwire.com.au</span></p>
    </div>
  </section>
</main>
</body>
</html>
```